cosmetic business needs inner and outer packaging

We, Velmora cosmetics, are a importer and oline retail of beauty products on an argan oil base. We will put 2 new products on the market.
A glass bottle 50ml of pure oil, and a 150g jar facemask.
Both need inner and outter packaging design.

Dimension of packaging:
Face mask jar:
- width : 20 cm - Height : 3 cm
Outter packaging:
- Width :  7,7 cm - height :  6,3 cm

Oil Bottle:
-Width : 10,4 cm - height : 4,3 cm
Outer packaging:
- Width :  3,8 cm - height :  12 cm

Pictures of the Jar & bottle are attached.

Our Brand:
Velmora design sources its products directly from the cooperatives in Morocco. The coorperatives are run by the local women. Therefore we support the local economy, independence of the woman and sustainable production.
We offer two classic beauty products. The pure argan oil, can be used for hair, skin or nails. It comes in a 50ml blue glass bottle.
A ghassoul face mask, comes in a jar of 150g.

For the design we envision a classicm, timeless design. Colours like lavendel, burgundy or indigo with specks of silver or gold. On the right side of the outter package we imagine an outline of what is inside. So a sillhouette of the jar/bottle.(see attached picture) But these are only ideas not limitations.
Attached some pictures of competitors.
If possible i would like to be able to amend the text as there cna be changes.

some competitors:
http://www.quendle.co.uk/
http://www.drpembrook.co.uk/03_face_oil.html
https://tessaborvik.com/

aldo obviously the logo has to be incoorperated in the packaging, so the bonus in the end will not demand any extra work

Target Market(s)

Taget marked:
Manily women, 26+ years, urban, interested in social and enviromental issues, earing money and able to spend on luxury products, interest in cosmetics,

Industry/Entity Type

Cosmetics

Logo Text

Velmora

Requirements
Must have
• amendable text on the back, as there are some legal requirements for cosmetic products.

```html
<!DOCTYPE html>
<html lang="en">
<head>
<meta charset="utf-8">
<title>Velmora Cosmetics – Argan Oil Packaging</title>
<link rel="stylesheet" href="https://fonts.googleapis.com/css2?family=Cinzel:wght@600;700&family=EB+Garamond:wght@400;500&display=swap">
<style>
  :root {
    --navy: #15213d;
    --navy-deep: #0f1930;
    --jar-blue: #1c2b6e;
    --bottle-blue: #1f2f86;
    --silver: #d9dbe0;
    --silver-soft: #aeb3bf;
    --pattern-light: rgba(170, 180, 205, 0.35);
    --page: #ffffff;
    --page-top: #ececec;
  }
  * { box-sizing: border-box; margin: 0; padding: 0; }
  html, body { width: 1200px; height: 790px; overflow: hidden; }
  body {
    position: relative;
    background: linear-gradient(180deg, var(--page-top) 0%, var(--page) 45%);
    font-family: "EB Garamond", serif;
    color: var(--silver);
  }
  .panel {
    position: absolute;
    background: var(--navy);
    overflow: hidden;
    text-align: center;
  }
  .pattern {
    position: absolute;
    border-radius: 50%;
    background: radial-gradient(circle, var(--pattern-light) 0%, rgba(170,180,205,0.15) 45%, rgba(170,180,205,0) 70%);
  }
  .brand {
    position: absolute;
    left: 0; right: 0;
    font-family: "EB Garamond", serif;
    font-weight: 500;
    text-transform: uppercase;
    letter-spacing: 0.04em;
    color: var(--silver);
  }
  .brand-mark {
    display: block;
    margin: 0 auto 6px;
    border: 1px solid var(--silver);
    border-radius: 50%;
  }
  .title {
    position: absolute;
    left: 0; right: 0;
    font-family: "Cinzel", serif;
    font-weight: 700;
    line-height: 1;
    color: var(--silver);
  }
  .title small { display: block; font-weight: 600; }
  .claim {
    position: absolute;
    left: 0; right: 0;
    line-height: 1.15;
  }
  .claim b {
    display: block;
    font-family: "Cinzel", serif;
    font-weight: 700;
  }
  .claim span { text-transform: uppercase; }
  .body-copy {
    position: absolute;
    color: var(--silver);
    line-height: 1.2;
  }

  /* Face mask outer box */
  .mask-box-side { left: 94px; top: 400px; width: 58px; height: 225px; background: var(--navy-deep); }
  .mask-box-side .body-copy { left: 6px; right: 6px; top: 14px; font-size: 6px; text-align: left; }
  .mask-box-side .ingredients { position: absolute; left: 4px; right: 4px; bottom: 24px; font-size: 6px; }
  .mask-box-front { left: 152px; top: 372px; width: 248px; height: 250px; }
  .mask-box-front .pattern { width: 220px; height: 220px; right: -110px; top: 20px; }
  .mask-box-front .pattern.low { left: -90px; top: 150px; width: 200px; height: 200px; }
  .mask-box-front .brand { top: 42px; font-size: 7px; }
  .mask-box-front .title { top: 158px; font-size: 24px; }
  .mask-box-front .title small { font-size: 13px; margin-bottom: 3px; }
  .mask-box-front .claim { top: 212px; }
  .mask-box-front .claim b { font-size: 9px; }
  .mask-box-front .claim span { font-size: 6px; }

  /* Face mask jar label */
  .jar-label { left: 436px; top: 456px; width: 260px; height: 156px; background: var(--jar-blue); border-radius: 4px; }
  .jar-label .pattern { width: 200px; height: 200px; top: -30px; }
  .jar-label .pattern.left { left: -120px; }
  .jar-label .pattern.right { right: -120px; }
  .jar-label .brand { top: 20px; font-size: 6px; }
  .jar-label .title { top: 78px; font-size: 21px; }
  .jar-label .title small { font-size: 12px; margin-bottom: 3px; }
  .jar-label .claim { top: 126px; }
  .jar-label .claim b { font-size: 8px; }
  .jar-label .claim span { font-size: 6px; }

  /* Oil bottle label */
  .bottle-label { left: 742px; top: 424px; width: 116px; height: 184px; background: var(--bottle-blue); }
  .bottle-label .pattern { width: 150px; height: 150px; left: -17px; top: 40px; }
  .bottle-label .brand { top: 14px; font-size: 5px; }
  .bottle-label .title { top: 120px; font-size: 19px; }
  .bottle-label .claim { top: 162px; }
  .bottle-label .claim b { font-size: 7px; }
  .bottle-label .claim span { font-size: 4px; }

  /* Oil outer box */
  .oil-box-front { left: 888px; top: 228px; width: 144px; height: 452px; }
  .oil-box-front .pattern { width: 200px; height: 200px; left: -28px; top: 160px; }
  .oil-box-front .brand { top: 40px; font-size: 8px; }
  .oil-box-front .title { top: 268px; font-size: 26px; }
  .oil-box-front .claim { top: 348px; }
  .oil-box-front .claim b { font-size: 9px; }
  .oil-box-front .claim span { font-size: 5px; }
  .oil-box-front .volume { position: absolute; left: 0; right: 0; top: 376px; font-size: 9px; }
  .oil-box-side { left: 1032px; top: 212px; width: 74px; height: 462px; background: var(--navy-deep); }
  .oil-box-side .pattern { width: 150px; height: 150px; left: -80px; top: 150px; }
  .oil-box-side .brand { top: 40px; font-size: 4px; }
  .oil-box-side .origin { position: absolute; left: 0; right: 0; top: 76px; font-size: 5px; text-transform: uppercase; }
  .oil-box-side .body-copy { left: 4px; right: 4px; top: 110px; font-size: 6.5px; text-align: center; }
  .oil-box-side .ingredients { position: absolute; left: 4px; right: 4px; top: 262px; font-size: 7px; line-height: 1.2; }
</style>
</head>
<body>

  <section class="panel mask-box-side" aria-label="Face mask box, side panel">
    <p class="body-copy">Velmora face mask blends pure argan oil with ghassoul clay to cleanse, soften and restore skin. Apply a thin layer, leave for ten minutes, then rinse with warm water.</p>
    <p class="ingredients">Ingredients:<br>100% Argan Oil</p>
  </section>

  <section class="panel mask-box-front" aria-label="Face mask box, front panel">
    <div class="pattern" role="img" aria-label="Silver mandala ornament"></div>
    <div class="pattern low" role="img" aria-label="Silver mandala ornament"></div>
    <div class="brand"><span class="brand-mark" style="width:16px;height:16px"></span>Velmora cosmetics</div>
    <h2 class="title"><small>Argan Oil</small>Face Mask</h2>
    <p class="claim"><b>ORGANIC</b><span>For all skin types</span></p>
  </section>

  <section class="panel jar-label" aria-label="Face mask jar label">
    <div class="pattern left" role="img" aria-label="Silver mandala ornament"></div>
    <div class="pattern right" role="img" aria-label="Silver mandala ornament"></div>
    <div class="brand"><span class="brand-mark" style="width:14px;height:14px"></span>Velmora cosmetics</div>
    <h2 class="title"><small>Argan Oil</small>Face Mask</h2>
    <p class="claim"><b>ORGANIC</b><span>For all skin types</span></p>
  </section>

  <section class="panel bottle-label" aria-label="Argan oil bottle label">
    <div class="pattern" role="img" aria-label="Silver mandala ornament"></div>
    <div class="brand"><span class="brand-mark" style="width:12px;height:12px"></span>Velmora cosmetics</div>
    <h2 class="title">Argan<br>Oil</h2>
    <p class="claim"><b>ORGANIC</b><span>For all skin and hair types</span></p>
  </section>

  <section class="panel oil-box-front" aria-label="Argan oil box, front panel">
    <div class="pattern" role="img" aria-label="Silver mandala ornament"></div>
    <div class="brand"><span class="brand-mark" style="width:18px;height:18px"></span>Velmora cosmetics</div>
    <h2 class="title">Argan<br>Oil</h2>
    <p class="claim"><b>ORGANIC</b><span>For all skin and hair types</span></p>
    <p class="volume">50ml</p>
  </section>

  <section class="panel oil-box-side" aria-label="Argan oil box, side panel">
    <div class="pattern" role="img" aria-label="Silver mandala ornament"></div>
    <div class="brand"><span class="brand-mark" style="width:10px;height:10px"></span>Velmora cosmetics</div>
    <p class="origin">Product of<br>Morocco</p>
    <p class="body-copy">Argan oil is a powerful anti-aging antioxidant. Great for treatment of all skin and hair types. Tazerine argan oil is ethically sourced from women-founded cooperatives that guarantee fair wages and sustainable practices to protect the argan forests of southwestern Morocco.</p>
    <p class="ingredients">Ingredients:<br>100% Argan Oil</p>
  </section>

</body>
</html>
```